Executive Presence Book Cover for Larkmoor Coaching

I am looking for 10 book covers that are unified and work very well together. they have to be simple with an international feel.I will be using the colors of the rainbows for the color of the books and all I am looking for is a creative way to write the title of the book on the cover. The ten titles are as follows: Transparency, Humility, Poise ,Charisma ,Relationships, Results, Clarity, Being Present, Grooming and Appearance,Acumen

Target Market(s)

business executives

Font styles to use
Other font styles liked:
• use any font you think would work

Colors

Designer to choose colors to be used in the design.

Requirements
Must have
• simple, easy to read, looking for the word to be the focus/focal point of the cover. we will be putting information on the back cover of our company etc.
• only the words of the title nothing else. The size of the book is 9“ x 7“. The only thing on the outside of the book is the title, no author nothing else. We will be putting information on the back cover of the book in very simple font.
Nice to have
• i would like each title of the 10 book covers to be clean, consistent and elegant and corporate. as long as it is not too "SILLY" i would like the titles to speak of their purpose. for instance,
• charisma could have a letter that look elegant
• being present could have some bold letters.
Should not have
• alot of drawings or pictures
• they can't be jovial, light or humorous treatments.

```html
<!DOCTYPE html>
<html lang="en">
<head>
<meta charset="utf-8">
<title>Appearance — Larkmoor Coaching Book Cover</title>
<link rel="stylesheet" href="https://fonts.googleapis.com/css2?family=Anton&display=swap">
<style>
  :root {
    --stage: #2a2a2a;
    --violet-deep: #8447a6;
    --violet-mid: #9a68b6;
    --violet-soft: #a983c2;
    --violet-light: #b495cc;
    --title-white: #ffffff;
    --title-shadow: rgba(60, 20, 80, 0.55);
  }
  html, body {
    margin: 0;
    padding: 0;
    width: 1145px;
    height: 1200px;
    overflow: hidden;
    background: var(--stage);
  }
  .book-cover {
    position: absolute;
    left: 106px;
    top: 0;
    width: 932px;
    height: 1200px;
    overflow: hidden;
  }
  .cover-texture {
    position: absolute;
    inset: 0;
    background:
      radial-gradient(ellipse 45% 30% at 8% 10%, var(--violet-deep) 0%, transparent 70%),
      radial-gradient(ellipse 40% 25% at 62% 30%, var(--violet-deep) 0%, transparent 70%),
      radial-gradient(ellipse 40% 28% at 92% 88%, var(--violet-deep) 0%, transparent 70%),
      radial-gradient(ellipse 35% 20% at 30% 100%, var(--violet-deep) 0%, transparent 70%),
      radial-gradient(ellipse 50% 40% at 80% 60%, var(--violet-light) 0%, transparent 70%),
      linear-gradient(160deg, var(--violet-mid) 0%, var(--violet-soft) 50%, var(--violet-mid) 100%);
  }
  .cover-title {
    position: absolute;
    left: 0;
    top: 0;
    width: 932px;
    height: 1200px;
    filter: drop-shadow(2px 4px 4px var(--title-shadow));
  }
  .cover-title text {
    font-family: "Anton", "Impact", sans-serif;
    font-size: 142px;
    fill: var(--title-white);
  }
</style>
</head>
<body>
  <main class="book-cover">
    <div class="cover-texture" role="img" aria-label="Faceted low-poly violet texture background"></div>
    <svg class="cover-title" viewBox="0 0 932 1200" xmlns="http://www.w3.org/2000/svg">
      <text x="61" y="291" textLength="810" lengthAdjust="spacingAndGlyphs">APPEARANCE</text>
    </svg>
  </main>
</body>
</html>
```